CEO of company needs clear business card that stands out from the rest

I need a clear business card (standard credit card size) for the CEO/Founder of our company...Brightfield Counseling. We would like to see designs that use our logo colors, which are khaki, chocolate brown, and gray. The card should be an edgy design, maybe where half the card is transparent with curves on the card, or a textured card where the logo is transparent, I don't care much for white cards. The final design should communicate a funky, edgy, and modern look, as well as stand out to have the "WOW" factor. The information we need on the card would be Name, Title, Toll free number, Phone Number, address, email address, and website.

*PLEASE SEND FRONT AND BACK OF CARDS

Card is two sided front and back please give us your front and back designs

The card should be an edgy design, maybe where half the card is transparent with curves on the card, or a textured card where the logo is transparent, I don't care much for white cards. The final design should communicate a funky, edgy, and modern look, as well as stand out to have the "WOW" factor.

Please follow these guidelines for the card

SPECS (card):

2.125 (h) x 3.375 (w) card size after cut

2.375 (h) x 3.625 (w) card with bleed

300 dpi

cmyk

1/8 bleed

allow 1/8 border for live area

I will also attached the pdf for the information listed above which includes a diagram of the card

 

All the cards need to have rounded edges

I just updated a card as an example of how you can use different fonts on a single business card, look how the name is written in script, so what I am saying is make this a card you will be proud to design and put it in your portfolio 

Reason: this race is really close and I am working with 2 designers to fine tune their designs and the weekend is slowing us down

• Our Logo
MUST HAVE PARTS OF CARD THAT ARE TRANSPARENT. See ideas that are attached.
Card is two sided front and back
• The final design should communicate a funky, edgy, and modern look, as well as stand out to have the "WOW" factor. The information we need on the card would be Name, Title, Toll free number, Phone Number, address, email address, and website.

```html
<!DOCTYPE html>
<html lang="en">
<head>
<meta charset="utf-8">
<title>Brightfield Counseling – Business Card</title>
<link href="https://fonts.googleapis.com/css2?family=Quicksand:wght@400;500;600&display=swap" rel="stylesheet">
<style>
  :root {
    --page-bg: #e9eaea;
    --card-clear: rgba(236, 240, 242, 0.78);
    --card-edge: rgba(255, 255, 255, 0.9);
    --panel-white: #fbfbfb;
    --chocolate: #7a4a26;
    --khaki: #b98a5e;
    --accent-fill: #d6c8bb;
    --gray: #8f8f8f;
    --gray-light: #b4b4b4;
  }
  * { margin: 0; padding: 0; box-sizing: border-box; }
  html, body {
    width: 1200px;
    height: 1000px;
    overflow: hidden;
    background: var(--page-bg);
    font-family: "Quicksand", sans-serif;
  }
  .card {
    position: absolute;
    left: 100px;
    top: 185px;
    width: 1000px;
    height: 630px;
    border-radius: 34px;
    background: linear-gradient(135deg, rgba(250,251,252,0.85), var(--card-clear) 60%, rgba(225,230,233,0.8));
    border: 2px solid var(--card-edge);
    box-shadow: 0 18px 40px rgba(0,0,0,0.08);
    overflow: hidden;
  }
  .holder {
    position: absolute;
    left: 40px;
    top: 40px;
  }
  .holder-name {
    font-size: 38px;
    font-weight: 600;
    color: var(--chocolate);
    line-height: 1.15;
  }
  .holder-title,
  .holder-email {
    font-size: 26px;
    font-weight: 400;
    color: var(--gray);
    line-height: 1.35;
  }
  .brand-panel {
    position: absolute;
    left: 0;
    top: 205px;
    width: 530px;
    height: 275px;
    background: var(--panel-white);
    border-radius: 0 30px 30px 0;
    display: flex;
    flex-direction: column;
    justify-content: center;
    padding-left: 40px;
  }
  .brand-row {
    display: flex;
    align-items: center;
    gap: 16px;
  }
  .brand-dot {
    width: 30px;
    height: 30px;
    border-radius: 50%;
    background: var(--khaki);
    flex: none;
  }
  .brand-name {
    font-size: 34px;
    font-weight: 500;
    color: var(--chocolate);
    line-height: 1.1;
    white-space: nowrap;
  }
  .brand-tagline {
    margin-top: 14px;
    margin-left: 46px;
    font-size: 24px;
    color: var(--gray);
    white-space: nowrap;
  }
  .accent-circle {
    position: absolute;
    left: 610px;
    top: 80px;
    width: 330px;
    height: 330px;
    border-radius: 50%;
    background: var(--accent-fill);
    opacity: 0.7;
  }
  .contact {
    position: absolute;
    left: 40px;
    bottom: 36px;
  }
  .toll-free {
    display: flex;
    align-items: center;
    gap: 8px;
  }
  .toll-label {
    font-size: 13px;
    font-weight: 600;
    color: var(--gray-light);
    line-height: 1;
    letter-spacing: 0.5px;
  }
  .toll-number {
    font-size: 38px;
    font-weight: 500;
    color: var(--chocolate);
    line-height: 1.1;
  }
  .address {
    font-size: 24px;
    color: var(--gray);
    margin-top: 4px;
    white-space: nowrap;
  }
  .website {
    position: absolute;
    right: 40px;
    bottom: 76px;
    font-size: 27px;
    font-weight: 600;
    color: var(--gray);
    white-space: nowrap;
  }
</style>
</head>
<body>
  <div class="card">
    <div class="holder">
      <p class="holder-name">Dana Whitlock</p>
      <p class="holder-title">CEO/Founder</p>
      <p class="holder-email">dwhitlock@brightfieldcounsel.com</p>
    </div>

    <div class="brand-panel">
      <div class="brand-row">
        <span class="brand-dot"></span>
        <span class="brand-name">Brightfield Counseling</span>
      </div>
      <p class="brand-tagline">a steady path to recovery</p>
    </div>

    <div class="accent-circle"></div>

    <div class="contact">
      <div class="toll-free">
        <span class="toll-label">TOLL<br>FREE</span>
        <span class="toll-number">1-800-555-0142</span>
      </div>
      <p class="address">45 Example Road, Anytown AZ 85000</p>
    </div>

    <p class="website">www.brightfieldcounsel.com</p>
  </div>
</body>
</html>
```